Letterhead Design Project

Initially, we would like to review our letterheads.

Something simple which uses our corporate imagery well and is nicely balanced.

Please note that I will be following up this letter-head with some customised quote templates and similarly customisable collateral in the next few weeks.

Target Market(s)

Enterprise business

Industry/Entity Type

Quote

Requirements
Must have
• The Nexora9 logo
See www.nexora9.com.au

Our tagline "Enterprise Hosting, Messaging and Server Virtualisation"

Our website address

Ideally in our colour pallette, but will consider submissions which look fantastic and necessitate other colours.

```html
<!DOCTYPE html>
<html lang="en">
<head>
<meta charset="utf-8">
<title>Nexora9 Letterhead</title>
<link href="https://fonts.googleapis.com/css2?family=Roboto+Condensed:wght@700&family=Open+Sans:wght@400&display=swap" rel="stylesheet">
<style>
  :root {
    --paper: #ffffff;
    --page-edge: #3a3a3a;
    --ink: #1d1d1b;
    --brand-red: #c11f33;
    --brand-pink: #e58a96;
    --brand-grey: #9a9a9a;
    --white: #ffffff;
  }
  * { margin: 0; padding: 0; box-sizing: border-box; }
  html, body {
    width: 1200px; height: 800px; overflow: hidden;
    background: var(--paper);
  }
  .canvas { position: relative; width: 1200px; height: 800px; }
  .letterhead {
    position: absolute; top: 32px;
    width: 522px; height: 736px;
    border: 1px solid var(--page-edge);
    background: var(--paper);
  }
  .letterhead--dark { left: 53px; --band: var(--ink); }
  .letterhead--red { left: 616px; --band: var(--brand-red); }

  .tagline-band {
    position: absolute; left: 1px; top: 21px;
    width: 288px; height: 38px;
    background: var(--band);
    color: var(--white);
    padding: 8px 6px 0 7px;
  }
  .tagline {
    font-family: "Roboto Condensed", sans-serif;
    font-weight: 700; font-size: 10.8px; letter-spacing: 0;
    white-space: nowrap; line-height: 13px;
  }
  .contact-line {
    font-family: "Open Sans", sans-serif;
    font-size: 8.6px; line-height: 12px;
    text-align: right; padding-right: 4px; white-space: nowrap;
  }
  .contact-line .divider {
    display: inline-block; width: 5px; height: 5px;
    background: var(--white); margin: 0 3px 1px; vertical-align: middle;
  }
  .accent-stripes {
    position: absolute; left: 295px; top: 21px;
    width: 14px; height: 38px;
    background: linear-gradient(90deg,
      var(--brand-grey) 0 4px, var(--paper) 4px 5px,
      var(--brand-red) 5px 8px, var(--paper) 8px 9px,
      var(--brand-pink) 9px 14px);
  }
  .brand-mark {
    position: absolute; left: 313px; top: 21px;
    width: 38px; height: 38px; background: var(--brand-red);
  }
  .brand-name {
    position: absolute; left: 358px; top: 17px;
    font-family: "Roboto Condensed", sans-serif;
    font-weight: 700; font-size: 42px; line-height: 46px;
    color: var(--ink); letter-spacing: -0.5px; white-space: nowrap;
  }
  .footer-rule {
    position: absolute; left: 113px; right: -1px; top: 711px;
    height: 5px;
    background: linear-gradient(90deg,
      var(--brand-pink) 0 2px, var(--ink) 2px 3px,
      var(--paper) 3px 5px, var(--brand-red) 5px 100%);
  }
</style>
</head>
<body>
<main class="canvas">
  <section class="letterhead letterhead--dark">
    <header>
      <div class="tagline-band">
        <p class="tagline">Enterprise Hosting, Messaging and Server Virtualisation</p>
        <p class="contact-line">www.nexora9.com.au<span class="divider"></span>info@nexora9.com.au</p>
      </div>
      <div class="accent-stripes"></div>
      <div class="brand-mark"></div>
      <p class="brand-name">Nexora9</p>
    </header>
    <div class="footer-rule"></div>
  </section>

  <section class="letterhead letterhead--red">
    <header>
      <div class="tagline-band">
        <p class="tagline">Enterprise Hosting, Messaging and Server Virtualisation</p>
        <p class="contact-line">www.nexora9.com.au<span class="divider"></span>info@nexora9.com.au</p>
      </div>
      <div class="accent-stripes"></div>
      <div class="brand-mark"></div>
      <p class="brand-name">Nexora9</p>
    </header>
    <div class="footer-rule"></div>
  </section>
</main>
</body>
</html>
```